Kestrel Bay Warehousing Group Needs A Website

We are looking for a website for a new company. 4 Pages

Needs to be responsive and mobile friendly for all browsers and coded for both Android & IOS. SEO is also important.

Website Brief – Kestrel Bay Warehousing Group
Domain: www.kestrelbaywarehousing.com
Email: info@kestrelbaywarehousing.com
Phone: to be inserted later
Address: 10458 82 Ave, Edmonton, AB T6E 2K9
Platform: WordPress (recommended for flexibility, SEO tools, and ease of editing)
Requirements:
• Responsive & mobile-friendly (Android & iOS)
• Cross-browser compatibility
• Fast page load speed
• SEO optimized for storage development, management, and investment keywords
• Easy in-house editing after launch
• Professional, modern, trust-driven design reflecting expertise, reliability, and innovation
________________________________________
Pages
1. HOME
Purpose: Quickly communicate who Kestrel Bay Warehousing Group is and why they’re the best choice for designing, building, leasing, and managing self storage facilities.
Content Highlights:
• Hero Section: Large, bold image of a modern self storage facility with headline:
"From Concept to Capacity – Your Self Storage Experts"
• Subheadline: “Kestrel Bay Warehousing Group delivers turnkey design, construction, leasing, and management services for profitable self storage operations.”
• Quick Service Icons:
o Facility Design & Development
o Construction & Build Management
o Lease-Up & Marketing
o Ongoing Facility Management
• Call to Action Button: “LEARN MORE” → links to ABOUT US page.
• Featured Project Highlights: Showcase a few completed or current projects with photos and stats.
• Contact Banner: “Ready to build your next self storage project? Let’s talk.” → CONTACT page.
2. ABOUT US
Purpose: Build credibility, showcase experience, and explain the value proposition.
Content Highlights:
• Who We Are: Overview of Kestrel Bay Warehousing Group’ history, mission, and team expertise.
• Our Approach: End-to-end process from site selection to occupancy.
• Why Choose Us:
o Industry expertise in self storage
o Proven track record in lease-up success
o Strong vendor and contractor network
3. SERVICES
Purpose: Detail all service offerings with clarity and authority.
Sections:
• Design & Development: Market analysis, site planning, and architectural design.
• Construction Management: Overseeing timelines, budgets, and quality control.
• Lease-Up Strategy: Marketing, promotions, and occupancy acceleration.
• Ongoing Facility Management: Staffing, maintenance, revenue optimization.

4. CONTACT
Purpose: Provide simple, direct ways to connect.
Content Highlights:
• Contact Form (Name, Email, Phone, Message)
• Direct Email: info@kestrelbaywarehousing.com
• Phone (if applicable)
• Google Map embed (if there’s a head office location)
• CTA: “Let’s Build Your Storage Success Story.”
Design & Technical Notes
• Visual Style: Clean, modern, bold typography, professional color palette (to be based on branding), strong imagery of self storage facilities.
• Performance: Image compression, caching, responsive scaling.
• SEO Targets: “Self storage facility developer,” “self storage construction,” “self storage management company,” “lease-up services for self storage.”

WordPress or Joomla – must be desktop and mobile friendly with fast page load speed. Need the ability to edit ourselves.

Use pantone colours - #033c5a – dark blue
#2baadf – light blue

```html
<!DOCTYPE html>
<html lang="en">
<head>
<meta charset="utf-8">
<title>Our Services – Kestrel Bay Warehousing Group</title>
<link href="https://fonts.googleapis.com/css2?family=Poppins:wght@300;400;500;600;700&display=swap" rel="stylesheet">
<style>
:root{
  --dark:#033c5a;
  --light:#2baadf;
  --mid:#0d4d6f;
  --text:#3d4c59;
  --white:#ffffff;
}
*{margin:0;padding:0;box-sizing:border-box}
html,body{width:1200px;height:3492px;overflow:hidden}
body{position:relative;background:var(--white);font-family:'Poppins',sans-serif;color:var(--text)}
.abs{position:absolute}

/* hero */
.hero-photo{left:0;top:0;width:1200px;height:630px;
  background:linear-gradient(115deg,#eef4f8 0%,#cfe1ee 30%,#8db6d6 55%,#3e78a8 78%,#21507a 100%)}
.hero-roof{left:0;top:0}
.site-header{left:83px;top:27px;width:1035px;height:68px;background:var(--white);display:flex;align-items:center;padding:0 28px}
.brand{display:flex;align-items:center;gap:8px;font-weight:600;color:var(--dark);font-size:15px;line-height:1.1;width:260px}
.brand-mark{width:14px;height:14px;background:var(--dark)}
.main-nav{display:flex;gap:0;margin-left:100px;height:68px}
.main-nav a{font-size:11px;font-weight:600;color:var(--dark);text-decoration:none;display:flex;align-items:center;height:68px;padding:0 17px;border-top:3px solid transparent}
.main-nav a.active{color:var(--light);border-top-color:var(--light)}
.page-title{left:83px;top:198px;font-size:50px;font-weight:700;color:var(--dark);line-height:1.05}
.intro{left:260px;top:580px;width:680px;text-align:center;font-size:17px;font-weight:500;line-height:27px;color:var(--dark)}

/* services */
.service-photo{display:block}
.service-text{width:370px}
.service-text h2{font-size:30px;font-weight:600;color:var(--dark);line-height:1.2;margin-bottom:14px;white-space:nowrap}
.service-text p{font-size:12px;line-height:17px;color:var(--text)}
.features{list-style:none;margin:22px 0 20px}
.features li{display:flex;gap:14px;margin-bottom:18px}
.feature-icon{flex:none;width:22px;height:18px;margin-top:2px}
.features h3{font-size:13.5px;font-weight:600;color:var(--dark);line-height:18px;margin-bottom:4px}
.features p{font-size:11px;line-height:16px}

/* cta */
.cta-band{left:83px;top:2803px;width:1034px;height:194px;background:var(--light)}
.cta-locker{left:146px;top:2739px}
.cta-title{left:397px;top:2844px;font-size:38px;font-weight:700;color:var(--white);line-height:52px}
.cta-button{left:908px;top:2879px;width:162px;height:43px;background:var(--white);color:var(--dark);font-size:11px;font-weight:600;display:flex;align-items:center;justify-content:center;text-decoration:none}

/* footer */
.footer-bg{left:0;top:2997px}
.footer-brand{left:0;top:3180px;width:1200px;text-align:center;color:var(--white);font-size:30px;font-weight:600;line-height:36px}
.footer-nav{left:0;top:3292px;width:1200px;display:flex;justify-content:center;gap:34px}
.footer-nav a{color:var(--white);font-size:11px;font-weight:600;text-decoration:none}
.social{left:539px;top:3334px;display:flex;gap:8px}
.social span{width:37px;height:37px;background:#1a587b;display:block}
.footer-rule{left:83px;top:3428px;width:1034px;height:1px;background:#2a6186}
.copyright{left:0;top:3452px;width:1200px;text-align:center;color:var(--white);font-size:10.5px}
.to-top{left:1143px;top:3403px;width:36px;height:41px}
</style>
</head>
<body>

<div class="abs hero-photo" role="img" aria-label="Modern glass office and storage building against a blue sky"></div>
<svg class="abs hero-roof" width="1200" height="700" viewBox="0 0 1200 700" aria-hidden="true">
  <polygon points="0,628 600,294 1200,628 1200,700 0,700" fill="#033c5a"/>
  <polygon points="0,700 0,630 600,362 1200,630 1200,700" fill="#ffffff"/>
</svg>

<header class="abs site-header">
  <div class="brand"><span class="brand-mark"></span>Kestrel Bay Warehousing Group</div>
  <nav class="main-nav">
    <a href="#">HOME</a><a href="#">ABOUT US</a><a href="#" class="active">SERVICES</a><a href="#">CONTACT</a>
  </nav>
</header>

<h1 class="abs page-title">Our<br>Services</h1>

<p class="abs intro">At Kestrel Bay Warehousing Group, we provide a full spectrum of services to take your self storage project from concept to ongoing success. Whether you’re building your first facility or expanding your portfolio, our team ensures every stage is handled with precision, efficiency, and a focus on profitability.</p>

<!-- Design & Development -->
<svg class="abs service-photo" style="left:113px;top:767px" width="516" height="437" viewBox="0 0 516 437" role="img" aria-label="Hands drafting building plans beside a yellow hard hat">
  <defs><linearGradient id="g1" x1="0" y1="0" x2="1" y2="1"><stop offset="0" stop-color="#e8d3b2"/><stop offset=".5" stop-color="#a99878"/><stop offset="1" stop-color="#4d5a55"/></linearGradient></defs>
  <polygon points="0,114 258,0 516,114 516,142 258,28 0,142" fill="#033c5a"/>
  <polygon points="0,162 258,42 516,162 516,437 0,437" fill="url(#g1)"/>
</svg>
<div class="abs service-text" style="left:720px;top:842px">
  <h2>Design &amp; Development</h2>
  <p>We start by laying a solid foundation for your project’s success. Our design and development services include:</p>
  <ul class="features">
    <li><svg class="feature-icon" viewBox="0 0 22 18"><rect x="2" y="2" width="16" height="14" fill="#2baadf"/></svg><div><h3>Market Analysis</h3><p>Understanding demand, competition, and ROI potential in your target area.</p></div></li>
    <li><svg class="feature-icon" viewBox="0 0 22 18"><rect x="2" y="2" width="16" height="14" fill="#2baadf"/></svg><div><h3>Site Planning</h3><p>Creating efficient layouts to maximize usable space and customer convenience.</p></div></li>
    <li><svg class="feature-icon" viewBox="0 0 22 18"><rect x="2" y="2" width="16" height="14" fill="#2baadf"/></svg><div><h3>Architectural Design</h3><p>Modern, secure, and visually appealing designs tailored to your brand.</p></div></li>
  </ul>
  <p>Our goal is to create facilities that stand out in the market and deliver long-term value.</p>
</div>

<!-- Construction Management -->
<div class="abs service-text" style="left:113px;top:1330px;width:400px">
  <h2>Construction Management</h2>
  <p>From groundbreaking to grand opening, we manage every<br>detail of the build. Our construction management includes:</p>
  <ul class="features">
    <li><svg class="feature-icon" viewBox="0 0 22 18"><rect x="2" y="2" width="16" height="14" fill="#2baadf"/></svg><div><h3>Timeline Oversight</h3><p>Ensuring milestones are met on schedule.</p></div></li>
    <li><svg class="feature-icon" viewBox="0 0 22 18"><rect x="2" y="2" width="16" height="14" fill="#2baadf"/></svg><div><h3>Budget Control</h3><p>Maximizing value without compromising quality.</p></div></li>
    <li><svg class="feature-icon" viewBox="0 0 22 18"><rect x="2" y="2" width="16" height="14" fill="#2baadf"/></svg><div><h3>Quality Assurance</h3><p>Partnering with trusted contractors and vendors to<br>maintain top standards.</p></div></li>
  </ul>
  <p>We take the stress out of construction so you can focus on your investment.</p>
</div>
<svg class="abs service-photo" style="left:570px;top:1265px" width="516" height="437" viewBox="0 0 516 437" role="img" aria-label="Construction team in safety vests reviewing plans on a laptop">
  <defs><linearGradient id="g2" x1="0" y1="0" x2="1" y2="1"><stop offset="0" stop-color="#c9c7c0"/><stop offset=".5" stop-color="#b8764a"/><stop offset="1" stop-color="#5a5550"/></linearGradient></defs>
  <polygon points="0,114 258,0 516,114 516,142 258,28 0,142" fill="#2baadf"/>
  <polygon points="0,162 258,42 516,162 516,437 0,437" fill="url(#g2)"/>
</svg>

<!-- Lease-Up Strategy -->
<svg class="abs service-photo" style="left:113px;top:1746px" width="516" height="437" viewBox="0 0 516 437" role="img" aria-label="Hand signing a lease beside a scale building model">
  <defs><linearGradient id="g3" x1="0" y1="0" x2="1" y2="1"><stop offset="0" stop-color="#f3ece0"/><stop offset=".55" stop-color="#c8bfb2"/><stop offset="1" stop-color="#28344a"/></linearGradient></defs>
  <polygon points="0,114 258,0 516,114 516,142 258,28 0,142" fill="#033c5a"/>
  <polygon points="0,162 258,42 516,162 516,437 0,437" fill="url(#g3)"/>
</svg>
<div class="abs service-text" style="left:720px;top:1852px">
  <h2>Lease-Up Strategy</h2>
  <p>Filling your units quickly is key to profitability. Our lease-up services help you achieve rapid occupancy with:</p>
  <ul class="features">
    <li><svg class="feature-icon" viewBox="0 0 22 18"><rect x="2" y="2" width="16" height="14" fill="#2baadf"/></svg><div><h3>Targeted Marketing</h3><p>Digital and local campaigns designed to attract the right customers.</p></div></li>
    <li><svg class="feature-icon" viewBox="0 0 22 18"><rect x="2" y="2" width="16" height="14" fill="#2baadf"/></svg><div><h3>Promotions &amp; Incentives</h3><p>Driving interest and increasing conversions.</p></div></li>
    <li><svg class="feature-icon" viewBox="0 0 22 18"><rect x="2" y="2" width="16" height="14" fill="#2baadf"/></svg><div><h3>Performance Tracking</h3><p>Monitoring occupancy rates and adjusting strategies for faster results.</p></div></li>
  </ul>
</div>

<!-- Facility Management -->
<div class="abs service-text" style="left:113px;top:2294px">
  <h2>Facility Management</h2>
  <p>Long-term success requires expert management. Our operational services include:</p>
  <ul class="features">
    <li><svg class="feature-icon" viewBox="0 0 22 18"><rect x="2" y="2" width="16" height="14" fill="#2baadf"/></svg><div><h3>Staffing &amp; Training</h3><p>Professional, customer-focused teams to run your facility.</p></div></li>
    <li><svg class="feature-icon" viewBox="0 0 22 18"><rect x="2" y="2" width="16" height="14" fill="#2baadf"/></svg><div><h3>Maintenance &amp; Upkeep</h3><p>Keeping your facility in top condition.</p></div></li>
    <li><svg class="feature-icon" viewBox="0 0 22 18"><rect x="2" y="2" width="16" height="14" fill="#2baadf"/></svg><div><h3>Revenue Optimization</h3><p>Pricing strategies, upsells, and operational efficiencies to maximize returns.</p></div></li>
  </ul>
  <p>We treat your facility like it’s our own—ensuring consistent growth and satisfied customers.</p>
</div>
<svg class="abs service-photo" style="left:570px;top:2228px" width="516" height="437" viewBox="0 0 516 437" role="img" aria-label="Two people carrying moving boxes in a storage facility hallway">
  <defs><linearGradient id="g4" x1="0" y1="0" x2="1" y2="1"><stop offset="0" stop-color="#c7a078"/><stop offset=".5" stop-color="#b9b2a8"/><stop offset="1" stop-color="#e4e2de"/></linearGradient></defs>
  <polygon points="0,114 258,0 516,114 516,142 258,28 0,142" fill="#033c5a"/>
  <polygon points="0,162 258,42 516,162 516,437 0,437" fill="url(#g4)"/>
</svg>

<!-- CTA -->
<div class="abs cta-band"></div>
<div class="abs cta-locker" role="img" aria-label="Open dark grey metal storage locker" style="width:207px;height:323px;background:linear-gradient(90deg,#2a2a2c,#4a4a4d 60%,#2f2f31)"></div>
<h2 class="abs cta-title">Ready to Build your Next<br>Self Storage Project?</h2>
<a class="abs cta-button" href="#">LET’S TALK</a>

<!-- Footer -->
<svg class="abs footer-bg" width="1200" height="495" viewBox="0 0 1200 495" aria-hidden="true">
  <polygon points="0,243 600,0 1200,243 1200,495 0,495" fill="#033c5a"/>
  <polygon points="0,330 600,70 1200,330 1200,410 600,150 0,410" fill="#11506f"/>
</svg>
<div class="abs footer-brand">Kestrel Bay<br>Warehousing Group</div>
<nav class="abs footer-nav"><a href="#">HOME</a><a href="#">ABOUT US</a><a href="#">SERVICES</a><a href="#">CONTACT</a></nav>
<div class="abs social"><span></span><span></span><span></span></div>
<div class="abs footer-rule"></div>
<p class="abs copyright">© Copyright 2025 Kestrel Bay Warehousing Group, All Rights Reserved</p>
<svg class="abs to-top" viewBox="0 0 36 41" aria-label="Back to top">
  <polygon points="0,12 18,0 36,12 36,41 0,41" fill="#2baadf"/>
  <path d="M18 30V16M12 21l6-6 6 6" stroke="#fff" stroke-width="2" fill="none"/>
</svg>

</body>
</html>
```